DESSERT MENU 11x17 *

Made to an authentic Spanish recipe, we cook our churros fresh to order. Crispy and golden, our churros are dusted in cinnamon or icing sugar and can be filled or served with a choice of dip-cups and extras.

1. Churro caramel ice cream - 8.99
2.brownie ice cream sundae - 8.95
3. flan - 2.99
4 cheese cake - 2.99
5. churros for 1 - 5.99
(3 churros , 1 dip )
6. churros for 2 - 9.95
( 6 churros , 2 dips)

dippings (hazelbliss , caramel , strawberry , chocolate )

glazed churros - 4.15
(white glaze , chocolate glaze , strawberry glaze )
add , sprinkles , coconut or chopped peanuts .

Requirements
Must have
• restautant logo .
• adress - 418 n. calloway ave
• alvora texas 78990
• 555-481-3067
Nice to have
• very colorful , remove the green background of logo ,still taking pics of glazed churros but the image should give an idea .

```html
<!DOCTYPE html>
<html lang="en">
<head>
<meta charset="utf-8">
<title>Tavo's Dessert Menu</title>
<link href="https://fonts.googleapis.com/css2?family=Comic+Neue:wght@400;700&family=Arimo:wght@400;700&display=swap" rel="stylesheet">
<style>
  :root {
    --green: #1e6a3a;
    --green-dark: #17572f;
    --orange: #eea322;
    --yellow: #f5e342;
    --ink: #1b1b1b;
    --paper: #fdfcfb;
    --stage: #e9e6e1;
    --white: #ffffff;
  }
  * { box-sizing: border-box; margin: 0; padding: 0; }
  html, body { width: 1200px; height: 1200px; overflow: hidden; }
  body {
    background: var(--stage);
    font-family: "Comic Neue", "Comic Sans MS", cursive;
    color: var(--ink);
  }
  .menu {
    position: absolute;
    left: 232px; top: 30px;
    width: 736px; height: 1140px;
    background: var(--paper);
    box-shadow: 0 6px 24px rgba(0,0,0,.25);
    overflow: hidden;
  }
  .awning { position: absolute; left: 0; top: 0; width: 736px; height: 44px; }

  .brand {
    position: absolute; left: 0; top: 120px; width: 736px;
    display: flex; justify-content: center; align-items: center; gap: 14px;
  }
  .brand-dot { width: 34px; height: 34px; border-radius: 50%; background: var(--orange); }
  .brand-name {
    font-size: 84px; font-weight: 700; color: var(--green); letter-spacing: 2px;
  }

  .ribbon { position: absolute; left: 204px; top: 250px; width: 330px; height: 66px; }
  .ribbon-title {
    position: absolute; left: 236px; top: 256px; width: 266px; height: 44px;
    display: flex; align-items: center; justify-content: center;
    font-size: 32px; font-weight: 700; color: var(--ink);
  }

  .item { position: absolute; width: 234px; height: 252px; }
  .item-photo {
    position: absolute; left: 3px; top: 0;
    width: 228px; height: 228px; border-radius: 50%;
    box-shadow: 0 2px 6px rgba(0,0,0,.18);
  }
  .item-price {
    position: absolute; right: -2px; top: -6px;
    width: 80px; height: 80px; border-radius: 50%;
    background: var(--green); border: 4px solid var(--white);
    display: flex; align-items: center; justify-content: center;
    color: var(--white); font-size: 29px; font-weight: 700;
    box-shadow: 0 2px 5px rgba(0,0,0,.2);
  }
  .item-label {
    position: absolute; left: 0; top: 193px; width: 234px; height: 57px;
    background: var(--orange); border: 3px solid var(--white); border-radius: 24px;
    display: flex; flex-direction: column; align-items: center; justify-content: center;
    font-size: 21px; font-weight: 700; line-height: 1.02; text-align: center;
    box-shadow: 0 2px 5px rgba(0,0,0,.2);
  }

  .col-1 { left: 13px; } .col-2 { left: 251px; } .col-3 { left: 489px; }
  .row-1 { top: 347px; } .row-2 { top: 626px; }

  .photo-caramel { background: radial-gradient(circle at 50% 55%, #f6efe3 0%, #e3a658 45%, #b2642a 80%, #f4f1ec 100%); }
  .photo-brownie { background: radial-gradient(circle at 50% 60%, #f7f1e8 0%, #7a4527 40%, #3d2015 75%, #f2efea 100%); }
  .photo-flan { background: radial-gradient(circle at 48% 50%, #f6dc8e 0%, #e4912a 40%, #f1eeea 75%, #dedbd6 100%); }
  .photo-cheesecake { background: radial-gradient(circle at 50% 55%, #fbf3dc 0%, #f1e5c0 40%, #cf2b2b 70%, #ebe8e4 100%); }
  .photo-churros-one { background: radial-gradient(circle at 55% 60%, #e9b86a 0%, #d68f3a 45%, #f3efe9 80%, #e5e2dd 100%); }
  .photo-churros-two { background: radial-gradient(circle at 50% 55%, #e6ad5e 0%, #cf8a34 45%, #f2efe9 80%, #e3e0db 100%); }

  .extras {
    position: absolute; left: 0; width: 736px; text-align: center; font-weight: 700;
  }
  .dips { top: 914px; font-size: 22px; }
  .glazed { top: 978px; font-size: 20px; }
  .glazed-price { font-size: 27px; }
  .glazed-flavours { top: 1012px; font-size: 16px; }
  .glazed-add { top: 1042px; font-size: 17px; }

  .contact {
    position: absolute; left: 11px; top: 1086px; width: 713px; height: 54px;
    background: var(--green); border-radius: 20px 20px 0 0;
    display: flex; align-items: center; justify-content: center; gap: 8px;
    font-family: "Arimo", Arial, sans-serif; color: var(--white); font-size: 18px;
    white-space: nowrap;
  }
  .contact strong { font-weight: 700; }
</style>
</head>
<body>
  <main class="menu">
    <svg class="awning" viewBox="0 0 736 44" aria-hidden="true">
      <g>
        <path d="M0 0h41v30a11 11 0 0 1-11 11H11A11 11 0 0 1 0 30z" fill="#eea322"/>
        <path d="M41 0h41v30a11 11 0 0 1-11 11H52A11 11 0 0 1 41 30z" fill="#1e6a3a"/>
        <path d="M82 0h41v30a11 11 0 0 1-11 11H93A11 11 0 0 1 82 30z" fill="#eea322"/>
        <path d="M123 0h41v30a11 11 0 0 1-11 11h-19a11 11 0 0 1-11-11z" fill="#1e6a3a"/>
        <path d="M164 0h41v30a11 11 0 0 1-11 11h-19a11 11 0 0 1-11-11z" fill="#eea322"/>
        <path d="M205 0h41v30a11 11 0 0 1-11 11h-19a11 11 0 0 1-11-11z" fill="#1e6a3a"/>
        <path d="M246 0h41v30a11 11 0 0 1-11 11h-19a11 11 0 0 1-11-11z" fill="#eea322"/>
        <path d="M287 0h41v30a11 11 0 0 1-11 11h-19a11 11 0 0 1-11-11z" fill="#1e6a3a"/>
        <path d="M328 0h41v30a11 11 0 0 1-11 11h-19a11 11 0 0 1-11-11z" fill="#eea322"/>
        <path d="M369 0h41v30a11 11 0 0 1-11 11h-19a11 11 0 0 1-11-11z" fill="#1e6a3a"/>
        <path d="M410 0h41v30a11 11 0 0 1-11 11h-19a11 11 0 0 1-11-11z" fill="#eea322"/>
        <path d="M451 0h41v30a11 11 0 0 1-11 11h-19a11 11 0 0 1-11-11z" fill="#1e6a3a"/>
        <path d="M492 0h41v30a11 11 0 0 1-11 11h-19a11 11 0 0 1-11-11z" fill="#eea322"/>
        <path d="M533 0h41v30a11 11 0 0 1-11 11h-19a11 11 0 0 1-11-11z" fill="#1e6a3a"/>
        <path d="M574 0h41v30a11 11 0 0 1-11 11h-19a11 11 0 0 1-11-11z" fill="#eea322"/>
        <path d="M615 0h41v30a11 11 0 0 1-11 11h-19a11 11 0 0 1-11-11z" fill="#1e6a3a"/>
        <path d="M656 0h41v30a11 11 0 0 1-11 11h-19a11 11 0 0 1-11-11z" fill="#eea322"/>
        <path d="M697 0h41v30a11 11 0 0 1-11 11h-19a11 11 0 0 1-11-11z" fill="#1e6a3a"/>
      </g>
    </svg>

    <div class="brand">
      <span class="brand-dot"></span>
      <span class="brand-name">TAVO'S</span>
    </div>

    <svg class="ribbon" viewBox="0 0 330 66" aria-hidden="true">
      <polygon points="0,28 40,28 40,64 0,64 18,46" fill="#f5e342" stroke="#1e6a3a" stroke-width="3"/>
      <polygon points="330,28 290,28 290,64 330,64 312,46" fill="#f5e342" stroke="#1e6a3a" stroke-width="3"/>
      <polygon points="34,52 70,52 70,64" fill="#17572f"/>
      <polygon points="296,52 260,52 260,64" fill="#17572f"/>
      <rect x="32" y="4" width="266" height="50" fill="#f5e342" stroke="#1e6a3a" stroke-width="4"/>
    </svg>
    <h1 class="ribbon-title">DESSERT MENU</h1>

    <section class="item col-1 row-1">
      <div class="item-photo photo-caramel" role="img" aria-label="Churros with vanilla ice cream, whipped cream and caramel drizzle"></div>
      <span class="item-price">8.99</span>
      <h2 class="item-label"><span>CHURRO CARAMEL</span><span>ICE CREAM</span></h2>
    </section>
    <section class="item col-2 row-1">
      <div class="item-photo photo-brownie" role="img" aria-label="Brownie topped with ice cream, chocolate and caramel sauce"></div>
      <span class="item-price">8.95</span>
      <h2 class="item-label"><span>BROWNIE ICE CREAM</span><span>SUNDAE</span></h2>
    </section>
    <section class="item col-3 row-1">
      <div class="item-photo photo-flan" role="img" aria-label="Caramel flan on a white plate with a spoon"></div>
      <span class="item-price">2.99</span>
      <h2 class="item-label"><span>FLAN</span></h2>
    </section>

    <section class="item col-1 row-2">
      <div class="item-photo photo-cheesecake" role="img" aria-label="Slice of cheesecake with strawberries and whipped cream"></div>
      <span class="item-price">2.99</span>
      <h2 class="item-label"><span>CHEESE CAKE</span></h2>
    </section>
    <section class="item col-2 row-2">
      <div class="item-photo photo-churros-one" role="img" aria-label="Three churros on a plate with a chocolate dip cup"></div>
      <span class="item-price">5.99</span>
      <h2 class="item-label"><span>CHURROS FOR 1</span><span>(3 churros, 1 dip )</span></h2>
    </section>
    <section class="item col-3 row-2">
      <div class="item-photo photo-churros-two" role="img" aria-label="Six churros on a platter with chocolate dip cups"></div>
      <span class="item-price">9.95</span>
      <h2 class="item-label"><span>CHURROS FOR 2</span><span>(6 churros, 2 dip )</span></h2>
    </section>

    <p class="extras dips">Dippings (hazelbliss, caramel, strawberry, chocolate )</p>
    <p class="extras glazed">Glazed churros - <span class="glazed-price">4.15</span></p>
    <p class="extras glazed-flavours">(White Glaze, Chocolate Glaze, Strawberry Glaze )</p>
    <p class="extras glazed-add">Add : Sprinkles, Coconut Or Chopped Peanuts .</p>

    <footer class="contact">
      <strong>CONTACT US : 555-481-3067</strong>
      <span>| 418 n. calloway ave, alvora texas 78990</span>
    </footer>
  </main>
</body>
</html>
```